Copperline Groundworks – Website Design Brief

Web Design Brief

We are seeking a web designer to build a modern, responsive website for Copperline Groundworks, a Sydney-based earthworks and excavation company.

2. Project Goal
- Build a professional, easy-to-navigate website that:
- Showcases CGW’s capabilities and past projects
- Attracts residential and commercial developers
- Builds credibility and encourages enquiries

3. Target Audience
- Residential developers and home builders
- Commercial construction firms
- Project managers seeking reliable excavation & plant hire services

4. Services to Highlight
- Bulk Excavation
- Detailed Excavation
- Demolition
- Shoring
- Plant Hire

5. Brand Style & Tone
- Clean, bold, and modern
- Professional with a “we get the job done” attitude
- Colors: Lime Green + Concrete Grey (from logo)
- Fonts: Match the modern, rounded, bold typeface in the logo
- Imagery: Showcase big machines, on-site work, before & after shots

6. Website Pages
Recommended structure:
- Home – Quick intro, project highlights, CTA
- About Us – Team story, mission, safety focus
- Services – Separate sections for each core service
- Projects – Case studies or photo gallery
- Plant Hire – Machines available, specs/photos
- Contact – Form + map + details

7. Assets Provided
- Logo (both long + stacked formats)
- Project photos. More can be provided if required.
- Copy: To be drafted

8. Deliverables
Responsive website (desktop/mobile/tablet)
- SEO-ready structure
- CMS (WordPress) for future edits
- Google Maps integration, job enquiry form

Target Market(s)

Target Audience Residential developers and home builders Commercial construction firms Project managers seeking reliable excavation & plant hire services

Industry/Entity Type

Construction

Number of Pages Required

1 page

Requirements
Must have
• Build a professional, easy-to-navigate website that: Showcases CGW’s capabilities and past projects Attracts residential and commercial developers Builds credibility and encourages enquiries
Nice to have
• All provided in the Description
Should not have

```html
<!DOCTYPE html>
<html lang="en">
<head>
<meta charset="utf-8">
<title>Copperline Groundworks – Earthworks &amp; Excavation</title>
<link href="https://fonts.googleapis.com/css2?family=Poppins:wght@300;400;500;600;700;800&display=swap" rel="stylesheet">
<style>
:root{
  --green:#7dbb42;
  --green-soft:#c8e3ad;
  --dark:#2e2e2e;
  --charcoal:#3a3a3a;
  --grey:#8a8a8a;
  --line:#e4e4e4;
  --white:#fff;
}
*{margin:0;padding:0;box-sizing:border-box}
html,body{width:1200px;height:3928px;overflow:hidden}
body{font-family:'Poppins',sans-serif;color:var(--dark);background:var(--white);position:relative}
.abs{position:absolute}
.btn{position:absolute;display:flex;align-items:center;justify-content:center;border-radius:20px;font-size:12px;font-weight:600;text-transform:uppercase;color:var(--white);background:var(--green)}
.btn.ghost{background:transparent;border:2px solid var(--green)}
.upper{text-transform:uppercase}

/* header */
.topbar{left:265px;top:0;width:935px;height:33px;background:#555;clip-path:polygon(20px 0,100% 0,100% 100%,0 100%);display:flex;align-items:center;padding-left:65px;gap:48px;color:#f0f0f0;font-size:12px}
.topbar span{display:flex;align-items:center;gap:7px}
.topbar .socials{position:absolute;right:30px;top:6px;display:flex;gap:8px}
.circ{width:20px;height:20px;border-radius:50%;border:1.5px solid #ddd}
.brand{left:111px;top:12px;width:160px;font-weight:800;font-size:26px;line-height:1;color:var(--green);text-transform:uppercase;letter-spacing:1px}
.nav{left:378px;top:63px;display:flex;align-items:center;gap:36px;font-size:12px;font-weight:500;color:#666;text-transform:uppercase}
.search{left:911px;top:56px;width:34px;height:34px;border-radius:50%;background:#777;display:flex;align-items:center;justify-content:center}
.header-line{left:0;top:109px;width:1200px;height:1px;background:var(--line)}

/* hero */
.hero{left:0;top:110px;width:1200px;height:614px;background:linear-gradient(100deg,#4c5150 0%,#6f7572 35%,#9aa39a 60%,#7d7a5e 78%,#5b4e3c 100%)}
.hero-title{left:86px;top:262px;font-size:82px;font-weight:800;color:var(--green);line-height:1}
.hero-sub{left:87px;top:360px;font-size:34px;font-weight:800;color:var(--white);line-height:1.2;text-transform:uppercase}
.hero-text{left:87px;top:448px;font-size:12.5px;color:#f2f2f2;line-height:1.5;width:400px}
.dots-hero{left:88px;top:579px;display:flex;gap:10px}
.dots-hero i{width:38px;height:3px;background:var(--green);display:block}
.dots-hero i.on{background:var(--white)}

/* section titles */
.sec-title{width:1200px;left:0;text-align:center;font-weight:700;text-transform:uppercase}
.label{font-size:13px;font-weight:600;color:var(--green);text-transform:uppercase}

/* services */
.card{width:242px;height:229px;border:1px solid #ddd;border-radius:12px;padding:26px 24px}
.card .ico{width:56px;height:56px;border-radius:50%;background:#e6f1da;margin-bottom:28px}
.card h3{font-size:14px;font-weight:600;text-transform:uppercase;margin-bottom:8px}
.card p{font-size:12px;line-height:1.5;color:var(--grey)}
.card.active{background:var(--green);border-color:var(--green)}
.card.active h3,.card.active p{color:var(--white)}
.card.active .ico{background:rgba(255,255,255,.25)}
.arrow{width:28px;height:28px;border-radius:50%;display:flex;align-items:center;justify-content:center}
.arrow.prev{background:#e9e9e9}
.arrow.next{background:var(--green)}

/* about */
.about-back{left:71px;top:1290px;width:400px;height:318px;background:var(--green-soft);border-radius:12px}
.about-img{left:89px;top:1273px;width:400px;height:360px;border-radius:12px;background:linear-gradient(160deg,#d4dbe2 0%,#b7bfc6 35%,#d59a2a 60%,#8b6b3a 100%)}
.about-h{left:540px;top:1298px;font-size:32px;font-weight:800;line-height:1.15;text-transform:uppercase}
.about-h em{font-style:normal;color:var(--green)}
.about-p{left:541px;top:1383px;width:430px;font-size:12.5px;line-height:1.45;color:var(--grey)}
.pillars{left:540px;top:1488px;display:flex}
.pillar{padding-right:20px;margin-right:20px;border-right:1px solid var(--line)}
.pillar:last-child{border:0}
.pillar h4{font-size:13px;font-weight:700;text-transform:uppercase;margin-bottom:6px}
.pillar p{font-size:12px;color:var(--grey);line-height:1.5}

/* projects */
.proj-band{left:0;top:1740px;width:1200px;height:307px;background:var(--green)}
.proj{top:1915px;width:250px;height:215px;border-radius:10px}
.dots{display:flex;gap:5px;align-items:center}
.dots i{width:7px;height:7px;border-radius:50%;background:var(--green-soft);display:block}
.dots i.on{width:12px;height:12px;border:2px solid var(--green);background:var(--white)}

/* plant hire */
.ph-h{left:88px;top:2278px;font-size:32px;font-weight:800;line-height:1.15;text-transform:uppercase}
.ph-p{left:88px;top:2358px;width:360px;font-size:12.5px;line-height:1.45;color:#555}
.machine{top:2423px;width:176px;height:160px;border-radius:10px;display:flex;align-items:flex-end;justify-content:center;padding-bottom:16px;color:var(--white);font-size:13px;font-weight:800;text-align:center;line-height:1.1;text-transform:uppercase}
.ph-back{left:752px;top:2257px;width:356px;height:358px;background:var(--green-soft);border-radius:12px}
.ph-img{left:732px;top:2239px;width:358px;height:358px;border-radius:12px;background:linear-gradient(170deg,#2fb3b5 0%,#2a9aa0 45%,#b36a25 68%,#4b3a2a 100%)}

/* testimonials */
.review{top:2813px;width:250px}
.review .who{display:flex;align-items:center;gap:10px;margin-bottom:22px}
.avatar{width:44px;height:44px;border-radius:50%;background:#d7d7d7}
.review strong{font-size:14px;font-weight:600;display:block}
.review small{font-size:9px;color:#555}
.stars{color:#f0a81c;font-size:11px;margin-right:4px}
.review p{font-size:12px;line-height:1.65;color:#555}

/* contact */
.cta-band{left:0;top:3180px;width:1200px;height:312px;background:var(--charcoal)}
.cta-img{left:34px;top:3103px;width:530px;height:443px;border-radius:40% 30% 10% 20%/40% 40% 20% 20%;background:linear-gradient(150deg,#f2c62a 0%,#e2b21f 45%,#7a6a4a 80%,#3c342a 100%)}
.cta-label{left:651px;top:3255px;font-size:13px;font-weight:700;color:var(--white);text-transform:uppercase}
.cta-h{left:650px;top:3278px;font-size:32px;font-weight:800;color:var(--white);text-transform:uppercase}
.cta-p{left:651px;top:3330px;width:470px;font-size:12.5px;line-height:1.45;color:#eee}

/* footer */
.f-brand{left:107px;top:3640px;width:210px;font-size:38px;font-weight:800;line-height:1.05;color:var(--green);text-transform:uppercase;letter-spacing:1px}
.f-social{left:144px;top:3792px;display:flex;gap:8px}
.f-social .circ{border-color:#666}
.f-col h5{font-size:17px;font-weight:500;color:var(--green);text-transform:uppercase;padding-bottom:8px;border-bottom:1px solid var(--line);display:inline-block;margin-bottom:10px}
.f-col li{list-style:none;font-size:12.5px;color:#444;line-height:22px;display:flex;align-items:center;gap:8px}
.news-p{font-size:12.5px;color:#444;line-height:1.4;margin-bottom:14px;width:270px}
.news-box{width:258px;height:48px;border-radius:24px;box-shadow:0 4px 14px rgba(0,0,0,.1);display:flex;align-items:center;padding:0 18px;gap:8px;font-size:10px;color:#999}
.f-line{left:120px;top:3873px;width:960px;height:1px;background:var(--line)}
.copy{left:0;top:3894px;width:1200px;text-align:center;font-size:12px;color:#444;text-transform:uppercase}
.totop{left:1112px;top:3855px;width:38px;height:38px;border-radius:50%;background:var(--green);display:flex;align-items:center;justify-content:center}
</style>
</head>
<body>

<!-- Header -->
<div class="abs topbar">
  <span><svg width="12" height="10" viewBox="0 0 12 10"><rect x="0.5" y="0.5" width="11" height="9" fill="none" stroke="#7dbb42"/><path d="M1 1l5 4 5-4" fill="none" stroke="#7dbb42"/></svg>info@copperlinegroundworks.com</span>
  <span><svg width="11" height="11" viewBox="0 0 24 24"><path d="M6 2l4 5-2 3a12 12 0 006 6l3-2 5 4-2 4C10 22 2 14 2 4z" fill="#7dbb42"/></svg>+(321)555-0148</span>
  <span><svg width="10" height="13" viewBox="0 0 10 13"><path d="M5 0a5 5 0 015 5c0 4-5 8-5 8S0 9 0 5a5 5 0 015-5z" fill="#7dbb42"/><circle cx="5" cy="5" r="2" fill="#555"/></svg>72 Ferris Rd. Marrickville, Australia</span>
  <div class="socials"><i class="circ" style="border-color:#7dbb42"></i><i class="circ"></i><i class="circ"></i><i class="circ"></i></div>
</div>
<div class="abs brand">Copperline<br>Groundworks</div>
<nav class="abs nav">
  <svg width="16" height="14" viewBox="0 0 16 14"><path d="M8 0l8 7h-2v7h-4V9H6v5H2V7H0z" fill="#7dbb42"/></svg>
  <span>About Us</span><span>Services</span><span>Projects</span><span>Plant Hire</span><span>Contact</span>
</nav>
<div class="abs search"><svg width="13" height="13" viewBox="0 0 13 13"><circle cx="5.5" cy="5.5" r="4.2" fill="none" stroke="#fff" stroke-width="1.6"/><path d="M8.6 8.6L12 12" stroke="#fff" stroke-width="1.6"/></svg></div>
<div class="btn" style="left:960px;top:56px;width:151px;height:34px">Get a Free Quote</div>
<div class="abs header-line"></div>

<!-- Hero -->
<section class="abs hero" role="img" aria-label="Yellow excavator digging on a cleared earthworks site under a grey sky"></section>
<h1 class="abs hero-title">SYDNEY’S</h1>
<h2 class="abs hero-sub">Trusted Earthworks &amp;<br>Excavation Experts</h2>
<p class="abs hero-text">Delivering reliable, high-performance excavation services for residential and commercial developments.</p>
<div class="btn" style="left:88px;top:508px;width:151px;height:34px">Get a Free Quote</div>
<div class="btn ghost" style="left:247px;top:508px;width:171px;height:34px">View Our Projects</div>
<div class="abs dots-hero"><i></i><i class="on"></i><i></i></div>

<!-- Services -->
<h2 class="abs sec-title" style="top:825px;font-size:30px">Services</h2>
<p class="abs sec-title" style="top:875px;font-size:12.5px;font-weight:400;color:var(--grey);text-transform:none">Each service gets a dedicated section with photos.</p>
<div class="abs arrow prev" style="left:33px;top:1029px"><svg width="10" height="8" viewBox="0 0 10 8"><path d="M9 4H1M4 1L1 4l3 3" fill="none" stroke="#aaa" stroke-width="1.3"/></svg></div>
<div class="abs arrow next" style="left:1137px;top:1029px"><svg width="10" height="8" viewBox="0 0 10 8"><path d="M1 4h8M6 1l3 3-3 3" fill="none" stroke="#fff" stroke-width="1.3"/></svg></div>
<article class="abs card" style="left:102px;top:926px"><div class="ico"></div><h3>Bulk Excavation</h3><p>We handle large-scale earth removal efficiently, preparing your site for development with precision and care.</p></article>
<article class="abs card active" style="left:354px;top:926px"><div class="ico"></div><h3>Plant Hire</h3><p>Modern equipment available for short- or long-term hire, with or without operators.</p></article>
<article class="abs card" style="left:605px;top:926px"><div class="ico"></div><h3>Demolition</h3><p>Safe and controlled demolition of structures, including clearance and waste management.</p></article>
<article class="abs card" style="left:857px;top:926px"><div class="ico"></div><h3>Shoring</h3><p>Professional shoring and retaining systems for structural safety and ground stability.</p></article>

<!-- About -->
<div class="abs about-back"></div>
<div class="abs about-img" role="img" aria-label="Yellow excavator with raised arm on a city building site"></div>
<h2 class="abs about-h">Built on <em>Precision,</em><br>Powered by Trust Body</h2>
<p class="abs about-p">Copperline Groundworks (CGW) is a Sydney-based earthworks and excavation company with a commitment to safety, quality, and getting the job done right — every time. With a skilled team and modern machinery, we support developers and builders from the ground up.</p>
<div class="abs pillars">
  <div class="pillar" style="width:190px"><h4>Our Mission</h4><p>At Copperline Groundworks, our<br>mission is simple:</p></div>
  <div class="pillar" style="width:166px"><h4>Our Team</h4><p>We’re a team of experienced operators, project</p></div>
  <div class="pillar"><h4>Commitment to Safety</h4><p>Safety isn’t just a<br>policy—it’s our culture.</p></div>
</div>
<div class="btn" style="left:540px;top:1577px;width:121px;height:33px">Read More</div>

<!-- Projects -->
<div class="abs proj-band"></div>
<p class="abs sec-title" style="top:1818px;font-size:13px;color:var(--white)">Projects</p>
<h2 class="abs sec-title" style="top:1840px;font-size:31px;color:var(--white)">Proven Results, Start to Finish</h2>
<div class="abs proj" style="left:90px;background:linear-gradient(170deg,#8fb8df 0%,#c9d6de 40%,#d28a35 65%,#8c7560 100%)" role="img" aria-label="Excavator clearing a site beside high-rise construction"></div>
<div class="abs proj" style="left:348px;background:linear-gradient(170deg,#9cbf6a,#6e9a3f)" role="img" aria-label="Grader on a site, shown under a green highlight"></div>
<div class="abs proj" style="left:605px;background:linear-gradient(170deg,#d8d0c4 0%,#c7a064 45%,#9a7444 100%)" role="img" aria-label="Wheel loader moving earth on a building site"></div>
<div class="abs proj" style="left:863px;background:linear-gradient(170deg,#5f8bc2 0%,#a5b9cc 40%,#d88c3e 65%,#c9b12a 100%)" role="img" aria-label="Excavator loading soil into a tipper truck"></div>
<div class="abs dots" style="left:573px;top:2155px"><i></i><i></i><i class="on"></i><i></i><i></i></div>

<!-- Plant Hire -->
<p class="abs label" style="left:88px;top:2254px">Plant Hire</p>
<h2 class="abs ph-h">Hire the Right<br>Machine for the Job</h2>
<p class="abs ph-p">All our plant equipment is well-maintained, modern, and available with skilled operators.</p>
<div class="abs machine" style="left:88px;background:linear-gradient(170deg,#eef1f3 0%,#c5b36b 55%,#5f5340 100%)" role="img" aria-label="Excavator fitted with rock breaker">Rock Breakers</div>
<div class="abs machine" style="left:271px;background:linear-gradient(170deg,#9fcb6a,#6c9c3b)" role="img" aria-label="Bobcat skid steer loader">Bobcats &amp;<br>Skid Steers</div>
<div class="abs machine" style="left:456px;background:linear-gradient(170deg,#c89a76 0%,#7fa0b0 50%,#3f5968 100%)" role="img" aria-label="Tipper truck on a quarry road">Tipper<br>Trucks – 10m3</div>
<div class="abs dots" style="left:335px;top:2599px"><i></i><i class="on"></i><i></i></div>
<div class="abs ph-back"></div>
<div class="abs ph-img" role="img" aria-label="Orange tracked excavator against a teal sky"></div>

<!-- Testimonials -->
<p class="abs sec-title label" style="top:2718px">Reviews</p>
<h2 class="abs sec-title" style="top:2740px;font-size:31px">Testimonials</h2>
<div class="abs arrow prev" style="left:33px;top:2911px"><svg width="10" height="8" viewBox="0 0 10 8"><path d="M9 4H1M4 1L1 4l3 3" fill="none" stroke="#aaa" stroke-width="1.3"/></svg></div>
<div class="abs arrow next" style="left:1137px;top:2911px"><svg width="10" height="8" viewBox="0 0 10 8"><path d="M1 4h8M6 1l3 3-3 3" fill="none" stroke="#fff" stroke-width="1.3"/></svg></div>
<div class="abs review" style="left:165px"><div class="who"><div class="avatar" role="img" aria-label="Reviewer portrait"></div><div><strong>Hannah L.</strong><small><span class="stars">★★★★★</span>1 month ago</small></div></div><p>I had my trailer hitch installed by the team at Ridgeway Hitch, and I couldn’t be happier! The installation was quick, and the staff was incredibly knowl-edgeable. I’ll definitely be coming back for more truck accessories</p></div>
<div class="abs review" style="left:473px"><div class="who"><div class="avatar" role="img" aria-label="Reviewer portrait"></div><div><strong>Tom &amp; Maria K.</strong><small><span class="stars">★★★★★</span>1 month ago</small></div></div><p>I had my trailer hitch installed by the team at Ridgeway Hitch, and I couldn’t be happier! The installation was quick, and the staff was incredibly knowl-edgeable. I’ll definitely be coming back for more truck accessories</p></div>
<div class="abs review" style="left:781px"><div class="who"><div class="avatar" role="img" aria-label="Reviewer portrait"></div><div><strong>Priya S.</strong><small><span class="stars">★★★★★</span>1 month ago</small></div></div><p>I had my trailer hitch installed by the team at Ridgeway Hitch, and I couldn’t be happier! The installation was quick, and the staff was incredibly knowl-edgeable. I’ll definitely be coming back for more truck accessories</p></div>

<!-- Contact CTA -->
<div class="abs cta-band"></div>
<div class="abs cta-img" role="img" aria-label="Yellow tracked excavator with bucket lowered"></div>
<p class="abs cta-label">Contact Page</p>
<h2 class="abs cta-h">Let’s Talk Earthworks</h2>
<p class="abs cta-p">Lorem Ipsum is simply dummy text of the printing and typesetting industry. Lorem Ipsum has been the industry's standard dummy text ever since the 1500s, when an unknown printer took a galley</p>
<div class="btn" style="left:651px;top:3397px;width:139px;height:33px">Send Enquiry</div>

<!-- Footer -->
<div class="abs f-brand">Copper<br>line<br>Ground</div>
<div class="abs f-social"><i class="circ"></i><i class="circ"></i><i class="circ"></i><i class="circ"></i></div>
<div class="abs f-col" style="left:365px;top:3630px"><h5>Quick Links</h5><ul><li>Home</li><li>About Us</li><li>Services</li><li>Projects</li><li>Plant Hire</li><li>Contact</li></ul></div>
<div class="abs f-col" style="left:564px;top:3630px"><h5>Contact Us</h5><ul>
  <li><svg width="10" height="10" viewBox="0 0 24 24"><path d="M6 2l4 5-2 3a12 12 0 006 6l3-2 5 4-2 4C10 22 2 14 2 4z" fill="#7dbb42"/></svg>+(321)555-0148</li>
  <li><svg width="11" height="9" viewBox="0 0 12 10"><rect x="0.5" y="0.5" width="11" height="9" fill="#7dbb42"/><path d="M1 1l5 4 5-4" fill="none" stroke="#fff"/></svg>info@copperlinegroundworks.com</li>
  <li><svg width="9" height="12" viewBox="0 0 10 13"><path d="M5 0a5 5 0 015 5c0 4-5 8-5 8S0 9 0 5a5 5 0 015-5z" fill="#7dbb42"/><circle cx="5" cy="5" r="2" fill="#fff"/></svg>72 Ferris Rd. Marrickville, Australia</li></ul></div>
<div class="abs f-col" style="left:847px;top:3630px"><h5>Newsletter</h5>
  <p class="news-p">Subscribe to our email address to get the latest news.</p>
  <div class="news-box"><svg width="11" height="9" viewBox="0 0 12 10"><rect x="0.5" y="0.5" width="11" height="9" fill="#7dbb42"/><path d="M1 1l5 4 5-4" fill="none" stroke="#fff"/></svg><span style="flex:1">Enter Your Email..</span><svg width="16" height="14" viewBox="0 0 16 14"><path d="M0 6L16 0 11 14 8 8z" fill="#7dbb42"/></svg></div>
</div>
<div class="abs f-line"></div>
<div class="abs totop"><svg width="10" height="7" viewBox="0 0 10 7"><path d="M1 6l4-4 4 4" fill="none" stroke="#fff" stroke-width="1.5"/></svg></div>
<p class="abs copy">© 2025 Copyright - Copperline Groundworks</p>

</body>
</html>
```